Tress Radiant from root to soul. Hair stylist that specializes in extensions.

I am Marisol I am a hair stylist and I would like a website designed for my hair business.

I currently book clients via my profile on glamslot.net/marisolbreck

I need a professional website ( tressradiantfromroottosoul.net ) to display photos and prices for services offered.

I would like to have a home page with a brief bio, Image with logo and testimonials at the bottom, and a header with tab that include: menu of services, gallery,and FAQs.

On the "Services" page, I'm not interested in photos on this page. Just the name of the service, brief description, and pricing. I would also like to have, on this page, "Appointment Request" with fields that include: Name, service requested, desired time frame (morning, afternoon, evening), and contact number and email

On the "Gallery" page, I would like pictures only, but arranged and/or presented in a creative way...

Target Market(s)

Women ages 25-55 who interested in hair extension services.

Industry/Entity Type

Hair And Beauty

Coding

Coded - Design and coding required

Number of Pages Required

5+ page

Font styles to use
Sans Serif

Requirements
Must have
• Must include tabs that include, Menu of services offered, a quik pae link to pay deposits with ease, location, contact information, photo gallery, and policy/faqs.
Nice to have
• If possible i would like to stream music with the ability to be silenced. I would like a neutral color palette tans and beige.
Should not have
• stock images

```html
<!DOCTYPE html>
<html lang="en">
<head>
<meta charset="utf-8">
<title>Tress Radiant from root to soul</title>
<link rel="stylesheet" href="https://fonts.googleapis.com/css2?family=Old+Standard+TT:wght@400;700&family=Open+Sans:ital,wght@0,400;0,600;1,400;1,600&display=swap">
<style>
:root{
  --orange:#fe9763;
  --peach:#f8d3c0;
  --aqua:#b3e6e3;
  --aqua-soft:#d1efec;
  --hero-grey:#e8e8e8;
  --ink:#1e1e2e;
  --text:#333;
  --muted:#6f6f6f;
  --white:#fff;
}
*{margin:0;padding:0;box-sizing:border-box}
html,body{width:1200px;height:3675px;overflow:hidden;background:var(--white)}
.canvas{position:relative;width:1200px;height:3675px;overflow:hidden;font-family:"Open Sans",sans-serif;color:var(--text)}
.abs{position:absolute}
.serif{font-family:"Old Standard TT",serif}

/* hero */
.hero{left:0;top:0;width:1200px;height:1035px;background:var(--hero-grey)}
.hero-art{left:0;top:0}
.side-bar{left:0;top:0;width:83px;height:681px;background:var(--orange)}
.menu-icon{left:26px;top:30px;width:24px;height:20px}
.menu-icon span{display:block;height:3px;background:var(--ink);margin-bottom:5px}
.aqua-patch{left:0;width:83px;background:var(--aqua)}
.brand-box{left:461px;top:0;width:278px;height:90px;background:#f0f0f0;text-align:center;padding-top:18px}
.brand-name{font-family:"Old Standard TT",serif;font-weight:700;font-size:30px;line-height:30px;color:var(--ink)}
.brand-tag{font-family:"Old Standard TT",serif;font-weight:700;font-size:9px;letter-spacing:1.5px;color:var(--ink);text-transform:uppercase}
.hero-title{left:161px;top:376px;font-size:46px;font-weight:700;color:var(--ink)}
.hero-sub{left:164px;top:434px;font-size:25px;color:var(--ink)}
.hero-by{left:164px;top:477px;font-size:17px;color:var(--ink);letter-spacing:.5px}
.dot{top:611px;width:6px;height:6px;border-radius:50%;background:rgba(255,255,255,.7)}
.dot.active{background:var(--ink)}
.bio-title{left:161px;top:753px;font-size:17px;font-weight:700;color:var(--ink);letter-spacing:.4px}
.bio-text{left:161px;top:778px;width:390px;font-size:11.6px;line-height:22.5px;font-style:italic;color:#444}

.divider{width:172px;height:6px;background:var(--ink);left:514px}
.section-title{width:1200px;left:0;text-align:center;font-family:"Old Standard TT",serif;font-weight:700;font-size:25px;color:var(--ink);letter-spacing:.5px}

/* testimonials */
.peach-band{left:0;top:1236px;width:1200px;height:345px;background:var(--peach)}
.client-photo{width:277px;height:279px;top:1194px}
.client-lower{width:277px;height:81px;top:1490px}
.accent{width:277px;height:7px;top:1473px;background:var(--orange)}
.arrow-btn{top:1353px;width:37px;height:38px;background:rgba(255,255,255,.75);display:flex;align-items:center;justify-content:center}
.quote{width:277px;top:1640px;border-top:2px solid var(--orange);padding-top:20px;text-align:center;font-style:italic;font-size:9.6px;line-height:18px;color:#666}
.quote .who{font-size:10.5px;color:#555;margin-bottom:2px}

/* services */
.services-band{left:0;top:1839px;width:1200px;height:941px;background:var(--aqua-soft)}
.service{width:330px;font-style:italic;font-size:9.8px;line-height:16px;color:#7a8a89}
.service h3{font-weight:600;font-size:12px;line-height:17px;color:#2d3340;font-style:italic}
.service .price{color:#2d3340;font-weight:600}
.form-title{width:1200px;left:0;top:2432px;text-align:center;font-size:16px;font-weight:700;color:var(--ink);letter-spacing:.5px}
.field{left:460px;width:278px;height:24px;border-bottom:1px solid #bfd9d6;font-size:13px;color:var(--ink);padding-top:4px}
.box{display:inline-block;width:9px;height:9px;border:1px solid var(--ink);margin:0 8px 0 3px;vertical-align:-1px}
.send{left:0;width:1200px;top:2645px;text-align:center;font-size:14px;font-weight:600;text-decoration:underline;color:var(--ink)}
.pay-box{left:502px;top:2688px;width:193px;height:52px;background:var(--white);border:1px solid #dde}
.pay-name{left:8px;top:2px;font-size:11px;font-style:italic;font-weight:600;color:#1e3a7a}
.card{top:22px;width:42px;height:24px;border-radius:3px}

/* faqs */
.faq{left:488px;top:2908px;font-size:10.3px;line-height:18px;font-style:italic;color:#333}
.faq .answer{padding-left:8px;color:#555}

/* contact */
.contact-band{left:0;top:3108px;width:1200px;height:567px;background:var(--orange)}
.info{left:0;width:1200px;text-align:center;font-size:10.4px;line-height:18px;color:#2b2b2b;text-transform:uppercase}
.info strong{font-weight:600}
.social{top:3563px;width:38px;height:38px;border-radius:50%;background:var(--ink);color:var(--orange);font-size:8.5px;font-weight:600;display:flex;align-items:center;justify-content:center}
</style>
</head>
<body>
<div class="canvas">

  <!-- HERO -->
  <section class="abs hero" aria-label="Featured">
    <svg class="abs hero-art" width="1200" height="1035" viewBox="0 0 1200 1035">
      <defs>
        <linearGradient id="portraitTone" x1="0" y1="0" x2="1" y2="1">
          <stop offset="0" stop-color="#e2b27a"/>
          <stop offset=".45" stop-color="#c98f55"/>
          <stop offset=".75" stop-color="#3a2a22"/>
          <stop offset="1" stop-color="#141414"/>
        </linearGradient>
      </defs>
      <polygon points="83,0 560,0 560,681 83,681" fill="#e6e6e6"/>
      <polygon points="83,0 520,0 560,560" fill="#f3f0ea"/>
      <rect x="83" y="681" width="1117" height="354" fill="#e9e9e9"/>
      <polygon role="img" aria-label="Portrait of a client with long golden wavy extensions" points="540,0 1200,0 1200,1035 520,1035 560,560" fill="url(#portraitTone)"/>
      <polygon points="560,560 1200,681 800,1035 520,1035" fill="rgba(20,20,20,.35)"/>
      <polygon points="640,300 1200,681 720,980" fill="rgba(230,230,225,.35)"/>
    </svg>
    <div class="abs side-bar"></div>
    <div class="abs menu-icon" aria-label="Menu"><span></span><span></span><span></span></div>
    <div class="abs aqua-patch" style="top:681px;height:30px"></div>
    <div class="abs aqua-patch" style="top:959px;height:73px"></div>

    <div class="abs brand-box">
      <div class="brand-name">Tress Radiant</div>
      <div class="brand-tag">from root to soul</div>
    </div>

    <h1 class="abs hero-title serif">8 Hairstyles 2016</h1>
    <p class="abs hero-sub serif">We've got hair ideas for days.</p>
    <p class="abs hero-by serif">by Marisol B.</p>
    <span class="abs dot active" style="left:565px"></span>
    <span class="abs dot" style="left:586px"></span>
    <span class="abs dot" style="left:609px"></span>
    <span class="abs dot" style="left:630px"></span>

    <h2 class="abs bio-title serif">Creative. Classic. Distinguished.</h2>
    <p class="abs bio-text">These are just a few attributes that Marisol embodies. received in depth training from Brightwell Academy of Hair Design, where I had the opportunity to pair my experience with advanced technical training. My passion for art and design has given me the opportunity to express myself through hair design. I also stay abreast of current trends through industry events, hair shows, and continuing education so that I can offer my clients the best services in hair care, style, and extensions.</p>
  </section>

  <!-- TESTIMONIALS -->
  <div class="abs divider" style="top:1033px"></div>
  <h2 class="abs section-title" style="top:1100px">Testemonials and Clients</h2>
  <div class="abs peach-band"></div>

  <div class="abs client-photo" role="img" aria-label="Client with long straight black hair" style="left:161px;background:linear-gradient(160deg,#d8d8d8,#b9b9b9 60%,#8c7a70)"></div>
  <div class="abs accent" style="left:161px"></div>
  <div class="abs client-lower" role="img" aria-label="Client outfit detail" style="left:161px;background:linear-gradient(180deg,#cfc9c3,#a9a39d)"></div>

  <div class="abs client-photo" role="img" aria-label="Client with long auburn curls" style="left:461px;background:linear-gradient(160deg,#d6d6d6,#b5a292 55%,#7b7470)"></div>
  <div class="abs accent" style="left:461px"></div>
  <div class="abs client-lower" role="img" aria-label="Client seated outfit detail" style="left:461px;background:linear-gradient(180deg,#8d8d8d,#3b3b3b)"></div>

  <div class="abs client-photo" role="img" aria-label="Client with honey ombre waves" style="left:762px;background:linear-gradient(160deg,#d4d4d4,#b08a68 55%,#6e5a4a)"></div>
  <div class="abs accent" style="left:762px"></div>
  <div class="abs client-lower" role="img" aria-label="Client seated on chair" style="left:762px;background:linear-gradient(180deg,#8a8a8a,#2f2f2f)"></div>

  <div class="abs arrow-btn" style="left:123px"><svg width="10" height="14" viewBox="0 0 10 14"><path d="M7 2 2 7l5 5" fill="none" stroke="#333" stroke-width="1.6"/></svg></div>
  <div class="abs arrow-btn" style="left:1039px"><svg width="10" height="14" viewBox="0 0 10 14"><path d="M3 2l5 5-5 5" fill="none" stroke="#333" stroke-width="1.6"/></svg></div>

  <div class="abs quote" style="left:161px"><div class="who">Danae R. / Dallas</div>"I have been looking for a stylist since I moved to Dallas for 7 years. I noticed a young ladys hair and she gave me Marisol information. I LOVE MY HAIR. She does an amazing job. Always leave satisfied!!!"</div>
  <div class="abs quote" style="left:461px"><div class="who">Kelsy M. / Dallas</div>"I never leave her shop disappointed! She's miracle worker to say the least :)"</div>
  <div class="abs quote" style="left:762px"><div class="who">Tamsin L. / Dallas</div>"Wonderful hairstylist that will keep your hair healthy and looking great."<br>Thank you!"</div>

  <!-- SERVICES -->
  <div class="abs services-band"></div>
  <div class="abs divider" style="top:1839px"></div>
  <h2 class="abs section-title" style="top:1896px">Services and Appointments</h2>

  <div class="abs service" style="left:290px;top:1972px"><h3>// Cleanse/ Style</h3>Thorough shampoo and conditioning services using Verdalle hair care products.<br><span class="price">$55 and up</span></div>
  <div class="abs service" style="left:678px;top:1972px"><h3>// Cleanse/ Style</h3>Thorough shampoo and conditioning services using Verdalle hair care products.<br><span class="price">$55 and up</span></div>
  <div class="abs service" style="left:290px;top:2071px"><h3>// Permanent Color</h3>ermanent coloring process which includes shampoo and conditioning services. Consultation is required and relaxed hair will not be permanently colored.<br><span class="price">$125 and up</span></div>
  <div class="abs service" style="left:678px;top:2071px"><h3>// Permanent Color</h3>ermanent coloring process which includes shampoo and conditioning services. Consultation is required and relaxed hair will not be permanently colored.<br><span class="price">$125 and up</span></div>
  <div class="abs service" style="left:290px;top:2186px"><h3>// Custom Extensions</h3>ull/Partial Sew In Extensions with cut and style included. Hair must be clean and free of products upon arrival. $25 … (more)<br><span class="price">$185 and up</span></div>
  <div class="abs service" style="left:678px;top:2186px"><h3>// Custom Extensions</h3>ull/Partial Sew In Extensions with cut and style included. Hair must be clean and free of products upon arrival. $25 … (more)<br><span class="price">$185 and up</span></div>
  <div class="abs service" style="left:290px;top:2285px"><h3>// Extension Removal</h3>Extensions are carefully removed, and hair is thoroughly cleansed and deep conditioned. Trim and style are included.<br><span class="price">$75 and up</span></div>
  <div class="abs service" style="left:678px;top:2285px"><h3>// Extension Removal</h3>Extensions are carefully removed, and hair is thoroughly cleansed and deep conditioned. Trim and style are included.<br><span class="price">$75 and up</span></div>

  <h3 class="abs form-title serif">Appointment Request</h3>
  <div class="abs field" style="top:2485px">name</div>
  <div class="abs field" style="top:2509px">service requested</div>
  <div class="abs field" style="top:2533px">/ morning<span class="box"></span> / afternoon<span class="box"></span> / evening<span class="box"></span></div>
  <div class="abs field" style="top:2557px">e-mail</div>
  <div class="abs field" style="top:2581px">contact number</div>
  <div class="abs send">send</div>

  <div class="abs pay-box">
    <span class="abs pay-name">Quik Pae</span>
    <span class="abs card" style="left:6px;background:#d9d9d9"></span>
    <span class="abs card" style="left:53px;background:#c7cbd6"></span>
    <span class="abs card" style="left:99px;background:#b9c2d8"></span>
    <span class="abs card" style="left:145px;background:#bcd3e6"></span>
  </div>

  <!-- FAQS -->
  <div class="abs divider" style="top:2780px"></div>
  <h2 class="abs section-title" style="top:2852px">Faqs</h2>
  <div class="abs faq">
    + How do I buy at Marisol Online?<br>
    + Can I buy online from anywhere in the world?<br>
    + Do I have to pay Custom Fees and Import Taxes?<br>
    - How can I pay my order?<br>
    <div class="answer">You'll be updated via email at each stage of the transfer. You can<br>also track your transfer with our award winning mobile apps and website wherever you are.</div>
    + Is it safe to shop at Marisol Online?<br>
    + In which currency do I make the payment?
  </div>

  <!-- CONTACT -->
  <div class="abs contact-band"></div>
  <div class="abs divider" style="top:3108px"></div>
  <h2 class="abs section-title" style="top:3148px">Contact</h2>
  <svg class="abs" style="left:588px;top:3206px" width="24" height="30" viewBox="0 0 24 30" aria-label="Location">
    <path d="M12 1C6 1 1.5 5.5 1.5 11.3 1.5 19 12 29 12 29s10.5-10 10.5-17.7C22.5 5.5 18 1 12 1z" fill="var(--ink)"/>
    <circle cx="12" cy="11" r="4.3" fill="var(--orange)"/>
  </svg>
  <div class="abs info" style="top:3252px">4180 Larkspur Ln, Suite 7<br>Dallas, TX, 75230<br>214-555-0147</div>
  <div class="abs info" style="top:3323px">+00 012 345 67 890<br>hello@tressradiant.net</div>
  <div class="abs info" style="top:3419px"><strong>Hours</strong><br>Tuesday &nbsp; 9:00AM - 6:00PM<br>Wednesday &nbsp; 9:00AM - 6:00PM<br>Thursday &nbsp; 9:00AM - 6:00PM</div>

  <div class="abs social" style="left:425px">Pals</div>
  <div class="abs social" style="left:487px">Chirp</div>
  <div class="abs social" style="left:549px">Folio</div>
  <div class="abs social" style="left:611px">Linkup</div>
  <div class="abs social" style="left:673px">Pinny</div>
  <div class="abs social" style="left:735px">Blog</div>

</div>
</body>
</html>
```